Pixel Orchard Services Flyer

I have a retail Computer Store that I want to promote in the local area.
The target market is seniors aged between 40-80 year olds. I need to create a flyer for the business to do a flyer drop to homes and business advertising the business & services we offer. I would also like to drop this on our socials for online target ads.
Store Name: Pixel Orchard systems Address: 48 Wrenfield Road, DONVALE Victoria 3111 Phone Number: (03) 9512 6407 Target Audience: older generation between 40 - 90 year olds Services offered: Retail Sales & Service, Complete Workshop Facilities, Cloud services, Workly 480 Experts, Network & Wireless Products, Managed Services, PC & Laptop Sales, Custom Built Computers Vendors: Kelvra, QTRAX, Lunadyne Partner, Ozly, Pexlo, JT & Quen Reseller Please keep it to A1 size and double sided with options to go A3 o A4 later.

Target Market(s)

Residential home users

Industry/Entity Type

www.pixelorchard.com.au

Font styles to use
Sans Serif

Colors
0054AA
0677BA
7BADD7
CADEEF
E8F1F8

Requirements
Must have
• Simple target is the elderly population

```html
<!DOCTYPE html>
<html lang="en">
<head>
<meta charset="utf-8">
<title>Pixel Orchard Systems Flyer</title>
<link rel="stylesheet" href="https://fonts.googleapis.com/css2?family=Russo+One&family=Barlow+Condensed:wght@500;600;700&display=swap">
<style>
  :root {
    --blue-deep: #0054AA;
    --blue-mid: #0677BA;
    --blue-soft: #7BADD7;
    --blue-pale: #CADEEF;
    --blue-mist: #E8F1F8;
    --navy: #1c3a8a;
    --navy-light: #23449c;
    --ink: #2b2b2b;
    --white: #ffffff;
    --backdrop: #676767;
  }
  * { margin: 0; padding: 0; box-sizing: border-box; }
  html, body { width: 846px; height: 1200px; overflow: hidden; background: var(--backdrop); }
  .spread {
    position: absolute;
    left: 8px;
    top: 315px;
    width: 1298px;
    height: 890px;
    transform: scale(0.64);
    transform-origin: 0 0;
    font-family: "Barlow Condensed", "Arial Narrow", sans-serif;
  }
  .page {
    position: absolute;
    top: 0;
    width: 638px;
    height: 890px;
    overflow: hidden;
    background: linear-gradient(160deg, var(--white) 0%, var(--blue-mist) 45%, var(--white) 85%);
  }
  .page--front { left: 0; }
  .page--back { left: 660px; }

  /* Front */
  .masthead { position: absolute; top: 50px; left: 0; width: 100%; text-align: center; }
  .masthead__name {
    font-family: "Russo One", sans-serif;
    font-size: 58px;
    line-height: 1;
    letter-spacing: 1px;
    color: var(--blue-mid);
  }
  .masthead__sub {
    margin-top: 10px;
    font-family: "Russo One", sans-serif;
    font-size: 32px;
    line-height: 1;
    letter-spacing: 6px;
    color: var(--ink);
  }
  .hero {
    position: absolute;
    top: 180px;
    left: 20px;
    width: 598px;
    height: 450px;
    background:
      radial-gradient(ellipse at 48% 38%, #7a45d6 0%, #4b3aa8 25%, rgba(75,58,168,0) 50%),
      radial-gradient(ellipse at 35% 88%, #c9ccd2 0%, rgba(201,204,210,0) 40%),
      linear-gradient(170deg, var(--blue-mist) 0%, var(--blue-pale) 60%, var(--white) 100%);
  }
  .brandline {
    position: absolute;
    left: 0;
    width: 100%;
    display: flex;
    justify-content: center;
    align-items: center;
    gap: 10px;
  }
  .page--front .brandline { top: 690px; }
  .brandline__mark { width: 34px; height: 34px; border-radius: 5px; background: var(--blue-deep); }
  .brandline__name {
    font-size: 30px;
    font-weight: 600;
    letter-spacing: 5px;
    text-transform: uppercase;
    color: var(--blue-deep);
  }

  /* Back */
  .services {
    position: absolute;
    top: 40px;
    left: 43px;
    width: 552px;
    height: 413px;
    border: 1px solid #8a8f99;
    border-radius: 24px;
    background: rgba(255,255,255,0.55);
  }
  .services__tab { position: absolute; top: -1px; left: 76px; }
  .services__title {
    position: absolute;
    top: 4px;
    left: 76px;
    width: 416px;
    text-align: center;
    font-size: 40px;
    font-weight: 700;
    color: var(--white);
    line-height: 56px;
  }
  .services__list {
    position: absolute;
    top: 80px;
    left: 24px;
    list-style: none;
  }
  .services__list li {
    display: flex;
    align-items: center;
    gap: 10px;
    height: 45.8px;
    font-size: 25px;
    font-weight: 600;
    color: var(--ink);
  }
  .services__monitor {
    position: absolute;
    top: 155px;
    left: 365px;
    width: 255px;
    height: 233px;
    background: linear-gradient(160deg, #eef1f4 0%, #f2c53a 40%, #2a6f8a 60%, #d9dde2 100%);
  }
  .page--back .brandline { top: 472px; }
  .intro { position: absolute; top: 530px; left: 0; width: 100%; text-align: center; }
  .intro__title { font-size: 28px; font-weight: 600; color: var(--blue-mid); line-height: 32px; }
  .intro__text {
    margin: 4px auto 0;
    width: 520px;
    font-size: 18px;
    font-weight: 500;
    line-height: 21.5px;
    color: var(--ink);
  }
  .vendors { position: absolute; top: 683px; left: 0; width: 100%; text-align: center; }
  .vendors__title { font-size: 34px; font-weight: 600; color: var(--blue-deep); line-height: 38px; }
  .vendors__list {
    margin: 8px auto 0;
    width: 540px;
    display: flex;
    justify-content: space-between;
    list-style: none;
    font-size: 24px;
    font-weight: 600;
    color: var(--blue-mid);
  }

  /* Footer */
  .footer { position: absolute; left: 0; top: 768px; width: 638px; height: 110px; }
  .footer > svg { position: absolute; inset: 0; }
  .footer__phone {
    position: absolute;
    left: 0;
    top: 56px;
    width: 262px;
    text-align: center;
    font-size: 36px;
    font-weight: 700;
    color: var(--white);
    letter-spacing: 0.5px;
  }
  .footer__contact {
    position: absolute;
    left: 306px;
    top: 38px;
    color: var(--white);
    font-size: 19px;
    font-weight: 600;
    line-height: 27px;
    list-style: none;
  }
  .footer__contact li { display: flex; align-items: center; gap: 7px; }
</style>
</head>
<body>
<div class="spread">

  <section class="page page--front">
    <header class="masthead">
      <h1 class="masthead__name">PIXEL ORCHARD</h1>
      <p class="masthead__sub">SYSTEMS</p>
    </header>

    <div class="hero" role="img" aria-label="Photo of a touchscreen all-in-one monitor on a silver stand with a hand touching the glowing purple screen, plus a small monitor, a laptop battery and a stand"></div>

    <div class="brandline">
      <span class="brandline__mark"></span>
      <span class="brandline__name">Pixel Orchard Systems</span>
    </div>

    <footer class="footer">
      <svg width="638" height="110" viewBox="0 0 638 110" aria-hidden="true">
        <rect x="0" y="25" width="638" height="85" fill="var(--navy-light)"/>
        <polygon points="0,0 252,0 276,56 262,110 0,110" fill="var(--navy)"/>
        <polyline points="258,2 282,56 268,108" fill="none" stroke="var(--blue-soft)" stroke-width="2"/>
        <circle cx="131" cy="32" r="13" fill="#4aa6e8" stroke="var(--white)" stroke-width="2"/>
        <path d="M126 25 q-2 2 0 7 q3 6 9 8 q4 1 5-1 l-3-3 q-1 1-3 0 q-3-2-5-5 q0-2 1-3 z" fill="var(--white)"/>
      </svg>
      <div class="footer__phone">(03) 9512 6407</div>
      <ul class="footer__contact">
        <li><svg width="11" height="14" viewBox="0 0 14 18" aria-hidden="true"><path d="M7 1a6 6 0 0 1 6 6c0 4-6 10-6 10S1 11 1 7a6 6 0 0 1 6-6z" fill="none" stroke="var(--blue-soft)" stroke-width="2"/><circle cx="7" cy="7" r="2" fill="var(--blue-soft)"/></svg>48 Wrenfield Road, DONVALE Victoria 3111</li>
        <li><svg width="12" height="12" viewBox="0 0 16 16" aria-hidden="true"><circle cx="8" cy="8" r="7" fill="none" stroke="var(--blue-soft)" stroke-width="1.5"/><ellipse cx="8" cy="8" rx="3" ry="7" fill="none" stroke="var(--blue-soft)" stroke-width="1.2"/><line x1="1" y1="8" x2="15" y2="8" stroke="var(--blue-soft)" stroke-width="1.2"/></svg>www.pixelorchard.com.au</li>
      </ul>
    </footer>
  </section>

  <section class="page page--back">
    <div class="services">
      <svg class="services__tab" width="416" height="68" viewBox="0 0 416 68" aria-hidden="true">
        <path d="M0 0 H416 Q392 6 380 40 Q372 66 350 66 H66 Q44 66 36 40 Q24 6 0 0 Z" fill="var(--navy)"/>
      </svg>
      <h2 class="services__title">SERVICES OFFERED</h2>
      <ul class="services__list">
        <li><svg width="14" height="14" viewBox="0 0 14 14" aria-hidden="true"><circle cx="7" cy="7" r="6" fill="none" stroke="var(--blue-mid)" stroke-width="1.4"/><path d="M4 7 l2 2 l4-4" fill="none" stroke="var(--blue-mid)" stroke-width="1.6"/></svg>Retail Sales &amp; Service</li>
        <li><svg width="14" height="14" viewBox="0 0 14 14" aria-hidden="true"><circle cx="7" cy="7" r="6" fill="none" stroke="var(--blue-mid)" stroke-width="1.4"/><path d="M4 7 l2 2 l4-4" fill="none" stroke="var(--blue-mid)" stroke-width="1.6"/></svg>Complete Workshop Facilities</li>
        <li><svg width="14" height="14" viewBox="0 0 14 14" aria-hidden="true"><circle cx="7" cy="7" r="6" fill="none" stroke="var(--blue-mid)" stroke-width="1.4"/><path d="M4 7 l2 2 l4-4" fill="none" stroke="var(--blue-mid)" stroke-width="1.6"/></svg>Cloud services</li>
        <li><svg width="14" height="14" viewBox="0 0 14 14" aria-hidden="true"><circle cx="7" cy="7" r="6" fill="none" stroke="var(--blue-mid)" stroke-width="1.4"/><path d="M4 7 l2 2 l4-4" fill="none" stroke="var(--blue-mid)" stroke-width="1.6"/></svg>Workly 480 Experts</li>
        <li><svg width="14" height="14" viewBox="0 0 14 14" aria-hidden="true"><circle cx="7" cy="7" r="6" fill="none" stroke="var(--blue-mid)" stroke-width="1.4"/><path d="M4 7 l2 2 l4-4" fill="none" stroke="var(--blue-mid)" stroke-width="1.6"/></svg>Network &amp; Wireless Products</li>
        <li><svg width="14" height="14" viewBox="0 0 14 14" aria-hidden="true"><circle cx="7" cy="7" r="6" fill="none" stroke="var(--blue-mid)" stroke-width="1.4"/><path d="M4 7 l2 2 l4-4" fill="none" stroke="var(--blue-mid)" stroke-width="1.6"/></svg>Managed Services</li>
        <li><svg width="14" height="14" viewBox="0 0 14 14" aria-hidden="true"><circle cx="7" cy="7" r="6" fill="none" stroke="var(--blue-mid)" stroke-width="1.4"/><path d="M4 7 l2 2 l4-4" fill="none" stroke="var(--blue-mid)" stroke-width="1.6"/></svg>PC &amp; Laptop Sales</li>
      </ul>
    </div>
    <div class="services__monitor" role="img" aria-label="Photo of a slim desktop monitor showing a flowing yellow and teal abstract wallpaper"></div>

    <div class="brandline">
      <span class="brandline__name">Pixel Orchard Systems</span>
    </div>

    <div class="intro">
      <h3 class="intro__title">NEW COMPUTER</h3>
      <p class="intro__text">Don't know where to start....? Don't know what you need....? Want to keep up with the latest in technology? We can help you. Whether you are a small or medium business, run a home office, or are a passionate “Gamer”, we can come up with the perfect solution to your computer needs</p>
    </div>

    <div class="vendors">
      <h3 class="vendors__title">Custom Built Computers Vendors</h3>
      <ul class="vendors__list">
        <li>Kelvra</li>
        <li>QTRAX</li>
        <li>Lunadyne Partner</li>
        <li>Ozly</li>
        <li>Pexlo</li>
        <li>JT</li>
        <li>Quen</li>
      </ul>
    </div>

    <footer class="footer">
      <svg width="638" height="110" viewBox="0 0 638 110" aria-hidden="true">
        <rect x="0" y="25" width="638" height="85" fill="var(--navy-light)"/>
        <polygon points="0,0 252,0 276,56 262,110 0,110" fill="var(--navy)"/>
        <polyline points="258,2 282,56 268,108" fill="none" stroke="var(--blue-soft)" stroke-width="2"/>
        <circle cx="131" cy="32" r="13" fill="#4aa6e8" stroke="var(--white)" stroke-width="2"/>
        <path d="M126 25 q-2 2 0 7 q3 6 9 8 q4 1 5-1 l-3-3 q-1 1-3 0 q-3-2-5-5 q0-2 1-3 z" fill="var(--white)"/>
      </svg>
      <div class="footer__phone">(03) 9512 6407</div>
      <ul class="footer__contact">
        <li><svg width="11" height="14" viewBox="0 0 14 18" aria-hidden="true"><path d="M7 1a6 6 0 0 1 6 6c0 4-6 10-6 10S1 11 1 7a6 6 0 0 1 6-6z" fill="none" stroke="var(--blue-soft)" stroke-width="2"/><circle cx="7" cy="7" r="2" fill="var(--blue-soft)"/></svg>48 Wrenfield Road, DONVALE Victoria 3111</li>
        <li><svg width="12" height="12" viewBox="0 0 16 16" aria-hidden="true"><circle cx="8" cy="8" r="7" fill="none" stroke="var(--blue-soft)" stroke-width="1.5"/><ellipse cx="8" cy="8" rx="3" ry="7" fill="none" stroke="var(--blue-soft)" stroke-width="1.2"/><line x1="1" y1="8" x2="15" y2="8" stroke="var(--blue-soft)" stroke-width="1.2"/></svg>www.pixelorchard.com.au</li>
      </ul>
    </footer>
  </section>

</div>
</body>
</html>
```